OLVAK Web Design (Need help to re-design our website)

We need someone to help us re-design our website and launch it. All contents for the website are ready. (https://olvak.example.au/)

-Rearrange categories:
1. Heating & Cooling
2. Remove Home Appliance
3. Remove Entertainment

Home page - redesign (It will be a nice touch if the banner is in the loop).

NOTE:
-Brand colour blue and orange.
-Try using professional fonts (Example: Helvetica, etc.)
-The website's Footer should be readable and use light colour.

Target Market(s)

Residentials & commercial buildings

Industry/Entity Type

Heat Ventilation and Cooling Industry, Technology , Renewables

Coding

Coded - Design and coding required

Colors
0094D4
00A9DD
6FCCEA
C7EBF8
E9F6FB
59FF00
82FF00
B8FF75
E3FFCB
F4FFEA
F0912C
F2A743
F7CA91
FBE8D2
FDF5EE

Requirements
Nice to have
• Effects/transition on the words/copy/images.

```html
<!DOCTYPE html>
<html lang="en">
<head>
<meta charset="utf-8">
<title>OLVAK – Heating, Cooling & Energy Solutions</title>
<link href="https://fonts.googleapis.com/css2?family=Roboto:wght@400;500;700&display=swap" rel="stylesheet">
<style>
:root{
  --blue:#1b5fb0;
  --blue-deep:#124c93;
  --orange:#f39426;
  --orange-soft:#f7a445;
  --dark:#222224;
  --grey:#f2f2f2;
  --cream:#fdf5ee;
  --cream-line:#fbe8d2;
  --text:#555;
  --white:#fff;
}
*{margin:0;padding:0;box-sizing:border-box}
html,body{width:1200px;height:3344px;overflow:hidden}
body{font-family:"Roboto",Helvetica,Arial,sans-serif;color:var(--text);background:var(--white);position:relative}
.abs{position:absolute}
a{color:inherit;text-decoration:none}

/* header */
.topbar{top:0;left:474px;height:30px;display:flex;font-size:13px;color:#fff}
.topbar div{display:flex;align-items:center;justify-content:center;gap:7px;height:30px}
.tb-phone{width:171px;background:var(--orange);clip-path:polygon(0 0,100% 0,100% 100%,12% 100%)}
.tb-mail{width:193px;background:var(--dark)}
.tb-book{width:217px;background:var(--blue);font-weight:700;clip-path:polygon(0 0,100% 0,92% 100%,0 100%)}
.logo{top:38px;left:144px;display:flex;align-items:center;gap:12px;font-size:36px;font-weight:700;color:var(--blue);letter-spacing:4px}
.logo i{width:34px;height:34px;background:var(--orange);border-radius:50%;display:block}
.nav{top:56px;right:145px;display:flex;align-items:center;gap:25px;font-size:14px;font-weight:500;color:#222}

/* hero */
.hero-wrap{top:100px;left:0;width:1200px;height:552px;background:linear-gradient(var(--white) 50%,var(--blue) 50%)}
.hero{width:100%;height:100%;border-bottom-right-radius:320px 300px;overflow:hidden;background:linear-gradient(100deg,#8f8c87 0%,#b9b3aa 45%,#d8d2c8 75%,#a8a29a 100%);position:relative}
.hero h1{position:absolute;top:112px;left:144px;font-size:42px;font-weight:500;color:#fff;letter-spacing:.5px}
.hero h1 span{color:var(--blue)}
.hero p{position:absolute;top:174px;left:144px;width:540px;font-size:16px;line-height:26px;color:#fff}
.btn{display:inline-flex;align-items:center;justify-content:center;gap:8px;font-weight:500;color:#fff;border-radius:0 22px 0 22px}
.hero .btn{position:absolute;top:253px;left:144px;width:174px;height:50px;background:var(--orange);font-size:16px}
.arrow{width:38px;height:38px;border-radius:50%;background:#222;display:flex;align-items:center;justify-content:center}

/* solutions */
.solutions{top:652px;left:0;width:1200px;height:600px;background:linear-gradient(160deg,#2a6bb8,#1b5fb0 50%,#1656a3);text-align:center;color:#fff}
.sec-title{font-size:33px;font-weight:500;letter-spacing:.3px}
.rule{display:block;width:120px;height:3px;background:#fff;margin:14px auto 0}
.solutions .sec-title{margin-top:68px}
.solutions .lead{margin-top:30px;font-size:17px;font-weight:500}
.cards{position:absolute;top:213px;left:0;width:100%}
.card{position:absolute;width:300px;text-align:center}
.card .ring{width:114px;height:114px;border-radius:50%;border:5px solid #f7b363;background:var(--orange);margin:0 auto;display:flex;align-items:center;justify-content:center}
.card h3{margin-top:33px;font-size:17px;font-weight:700}
.card p{margin-top:14px;font-size:13.5px;line-height:23px}
.card .btn{margin-top:22px;width:120px;height:37px;border:2px solid #fff;font-size:14px}

/* about */
.about-wrap{top:1216px;left:0;width:1200px;height:557px;background:linear-gradient(var(--blue) 50%,var(--orange) 50%)}
.about{width:100%;height:100%;background:#fff;border-top-left-radius:190px 140px;border-bottom-right-radius:280px 240px;position:relative}
.about .block{position:absolute;top:291px;left:122px;width:178px;height:200px;background:var(--blue)}
.about .photo{position:absolute;top:80px;left:144px;width:408px;height:394px;background:linear-gradient(180deg,#e6e2dc,#cfc8be 60%,#8f8780);border-bottom-right-radius:30px}
.about h2{position:absolute;top:118px;left:619px;font-size:33px;font-weight:500;color:#222;display:flex;align-items:center;gap:16px}
.about h2::after{content:"";width:68px;height:3px;background:var(--orange)}
.about .copy{position:absolute;top:172px;left:619px;width:436px;font-size:13.5px;line-height:25px;text-align:justify}
.about .copy p+p{margin-top:7px}
.about .btn{position:absolute;top:379px;left:619px;width:150px;height:43px;background:var(--orange);font-size:14px}

/* question */
.question{top:1773px;left:0;width:1200px;height:357px;background:linear-gradient(90deg,#f28c1f,#f6a341 50%,#f28c1f);text-align:center;color:#fff}
.question .sec-title{margin-top:48px}
.question .rule{width:90px}
.question .lead{margin:30px auto 0;width:820px;font-size:13.5px;line-height:24px}
.help{position:absolute;top:250px;left:327px;display:flex;align-items:center;gap:14px;text-align:left}
.help .ic{width:40px;height:40px;border-radius:50%;background:var(--blue);display:flex;align-items:center;justify-content:center;border:3px solid #fff}
.help small{display:block;font-size:15px;font-weight:500}
.help strong{display:block;font-size:23px;font-weight:500;margin-top:3px}
.question .btn{position:absolute;top:253px;left:708px;width:164px;height:39px;background:var(--blue);font-size:14px;font-weight:700}

/* categories */
.cat-wrap{top:2130px;left:0;width:1200px;height:460px;background:linear-gradient(var(--orange) 50%,var(--grey) 50%)}
.cat{width:100%;height:100%;background:#fff;border-top-left-radius:190px 130px;border-bottom-right-radius:300px 200px;position:relative}
.tabs{position:absolute;top:137px;left:147px;width:232px}
.tab{height:54px;display:flex;align-items:center;padding-left:28px;font-size:19px;font-weight:500;color:#222}
.tab.active{background:var(--blue);color:#fff;border-left:5px solid var(--orange);padding-left:23px}
.panel{position:absolute;top:74px;left:431px;width:622px;height:298px;background:#fff;box-shadow:0 4px 18px rgba(0,0,0,.16);border-radius:0 0 16px 0}
.panel .photo{position:absolute;top:7px;left:7px;width:343px;height:286px;background:linear-gradient(120deg,#a9cddd,#4f8aa6 45%,#173848 75%,#0c1d26)}
.panel .info{position:absolute;top:30px;left:381px}
.panel h3{margin-top:22px;font-size:19px;font-weight:500;color:#222}
.panel ul{list-style:none;margin-top:18px}
.panel li{display:flex;align-items:center;gap:11px;font-size:13px;height:31px}
.panel li i{width:12px;height:12px;border-radius:50%;background:var(--blue);display:inline-block;position:relative}
.panel li i::after{content:"";position:absolute;left:4px;top:2px;width:3px;height:6px;border:solid #fff;border-width:0 1.5px 1.5px 0;transform:rotate(45deg)}

/* rebates */
.rebates{top:2590px;left:0;width:1200px;height:450px;background:var(--grey);text-align:center}
.rebates .sec-title{margin-top:65px;font-size:31px;color:#222}
.rebates .rule{width:252px;background:var(--orange)}
.badge{position:absolute;top:163px;width:208px;height:208px}

/* footer (light) */
.footer-wrap{top:3040px;left:0;width:1200px;height:263px;background:var(--grey)}
.footer{width:100%;height:100%;background:var(--cream);border-top:3px solid var(--orange);border-top-left-radius:170px 130px;position:relative;color:#333}
.footer h4{position:absolute;top:66px;font-size:17px;font-weight:700;color:var(--blue)}
.links{position:absolute;top:101px;left:148px;list-style:none;font-size:13px;line-height:24px}
.contact{position:absolute;top:105px;left:473px;font-size:13px}
.contact div{display:flex;gap:12px;align-items:flex-start}
.contact div+div{margin-top:16px}
.contact i{width:22px;height:22px;border-radius:50%;background:var(--blue);flex:none;display:flex;align-items:center;justify-content:center}
.contact span{line-height:23px}
.sub-text{position:absolute;top:101px;left:818px;width:240px;font-size:13px;line-height:20px}
.sub{position:absolute;top:152px;left:818px;width:235px;height:34px;background:#fff;border:1px solid var(--cream-line);border-radius:17px;overflow:hidden;display:flex}
.sub span{flex:1;font-size:10px;color:#777;display:flex;align-items:center;padding-left:14px}
.sub b{width:46px;background:var(--orange);display:flex;align-items:center;justify-content:center}
.social{position:absolute;top:207px;left:813px;display:flex;gap:11px}
.social i{width:28px;height:28px;border-radius:50%;background:var(--blue);display:block}
.social i:nth-child(2){background:var(--orange)}
.bottombar{top:3303px;left:0;width:1200px;height:41px;background:var(--blue);color:#fff;font-size:13px;display:flex;align-items:center;justify-content:space-between;padding:0 146px}
.bottombar u{font-weight:700}
</style>
</head>
<body>

<header>
  <div class="abs topbar">
    <div class="tb-phone"><svg width="12" height="12" viewBox="0 0 24 24"><path fill="#fff" d="M6.6 10.8a15 15 0 0 0 6.6 6.6l2.2-2.2c.3-.3.7-.4 1-.2 1.1.4 2.3.6 3.6.6.6 0 1 .4 1 1V20c0 .6-.4 1-1 1A17 17 0 0 1 3 4c0-.6.4-1 1-1h3.5c.6 0 1 .4 1 1 0 1.3.2 2.5.6 3.6.1.3 0 .7-.2 1z"/></svg>18000 52417</div>
    <div class="tb-mail"><svg width="13" height="10" viewBox="0 0 26 20"><path fill="#fff" d="M0 0h26v20H0z"/><path d="M2 2l11 8 11-8" stroke="#222" stroke-width="2" fill="none"/></svg>info@olvak.example.au</div>
    <div class="tb-book"><svg width="12" height="12" viewBox="0 0 24 24"><rect x="2" y="4" width="20" height="18" rx="2" fill="none" stroke="#fff" stroke-width="2.5"/><path d="M2 9h20M7 1v5M17 1v5" stroke="#fff" stroke-width="2.5"/></svg>Book Appointment</div>
  </div>
  <a class="abs logo" href="https://olvak.example.au/"><i></i>OLVAK</a>
  <nav class="abs nav">
    <a>Home</a><a>Heating &amp; Cooling</a><a>Our Story</a><a>Support</a>
    <svg width="14" height="14" viewBox="0 0 24 24"><circle cx="10" cy="10" r="7" fill="none" stroke="#222" stroke-width="3"/><path d="M15 15l7 7" stroke="#222" stroke-width="3"/></svg>
  </nav>
</header>

<section class="abs hero-wrap">
  <div class="hero" role="img" aria-label="Room furnished with a wall air conditioner, heat pump units and modern home electronics">
    <h1>WELCOME TO <span>OLVAK</span></h1>
    <p>Our mission is to help individuals and businesses their carbon footprint while also enhancing their comfort and quality of life.</p>
    <a class="btn">Explore Now <svg width="15" height="15" viewBox="0 0 24 24"><circle cx="12" cy="12" r="11" fill="#fff"/><path d="M10 7l5 5-5 5" stroke="#f39426" stroke-width="3" fill="none"/></svg></a>
    <div class="abs arrow" style="top:263px;left:55px"><svg width="14" height="14" viewBox="0 0 24 24"><path d="M15 5l-7 7 7 7" stroke="#fff" stroke-width="3" fill="none"/></svg></div>
    <div class="abs arrow" style="top:263px;left:1099px"><svg width="14" height="14" viewBox="0 0 24 24"><path d="M9 5l7 7-7 7" stroke="#fff" stroke-width="3" fill="none"/></svg></div>
  </div>
</section>

<section class="abs solutions" role="img" aria-label="Blue tinted background of people relaxing at home">
  <h2 class="sec-title">OFFERING SOLUTIONS FOR</h2>
  <span class="rule"></span>
  <p class="lead">Please select from a category below that best suits your requirements.</p>
  <div class="cards">
    <div class="card" style="left:117px">
      <div class="ring"><svg width="58" height="58" viewBox="0 0 60 60" fill="none" stroke="#fff" stroke-width="2.5"><path d="M6 30L30 9l24 21M12 25v28h36V25"/><rect x="18" y="36" width="10" height="17"/><rect x="33" y="34" width="10" height="9"/></svg></div>
      <h3>RESIDENTIAL</h3>
      <p>If you're enquiring ab out any product related<br>to your home usage, please contact us.</p>
      <a class="btn">Explore <svg width="13" height="13" viewBox="0 0 24 24"><circle cx="12" cy="12" r="11" fill="#fff"/><path d="M10 7l5 5-5 5" stroke="#1b5fb0" stroke-width="3" fill="none"/></svg></a>
    </div>
    <div class="card" style="left:431px">
      <div class="ring"><svg width="58" height="58" viewBox="0 0 60 60" fill="none" stroke="#fff" stroke-width="2.5"><path d="M10 14h34l-5-5M50 24H16l5 5M8 36l10-6h10l8 6 8-4 8 6-12 10H22l-8-6H8z"/></svg></div>
      <h3>TRADE</h3>
      <p>If you're enquiring about any product related<br>to your trade business, please contact us.</p>
      <a class="btn">Explore <svg width="13" height="13" viewBox="0 0 24 24"><circle cx="12" cy="12" r="11" fill="#fff"/><path d="M10 7l5 5-5 5" stroke="#1b5fb0" stroke-width="3" fill="none"/></svg></a>
    </div>
    <div class="card" style="left:751px">
      <div class="ring"><svg width="58" height="58" viewBox="0 0 60 60" fill="none" stroke="#fff" stroke-width="2.5"><rect x="14" y="10" width="32" height="44"/><path d="M20 6h20M8 54h44M20 18h6M34 18h6M20 28h6M34 28h6M20 38h6M34 38h6M26 54V46h8v8"/></svg></div>
      <h3>COMMERCIAL</h3>
      <p>If you're enquiring about any product related to<br>your business requirements, please contact us.</p>
      <a class="btn">Explore <svg width="13" height="13" viewBox="0 0 24 24"><circle cx="12" cy="12" r="11" fill="#fff"/><path d="M10 7l5 5-5 5" stroke="#1b5fb0" stroke-width="3" fill="none"/></svg></a>
    </div>
  </div>
</section>

<section class="abs about-wrap">
  <div class="about">
    <div class="block"></div>
    <div class="photo" role="img" aria-label="Woman relaxing on a sofa beneath a wall air conditioner"></div>
    <h2>ABOUT US</h2>
    <div class="copy">
      <p>OLVAK is a company dedicated to manufacturing and installing energy-efficient products that reduce energy consumption, save costs, and promote sustainability. Our mission is to help individuals and businesses reduce their carbon footprint while also enhancing their comfort.</p>
      <p>Our story began with a group of like-minded individuals who saw the urgent need to address climate change and the impact of energy consumption on the environment.</p>
    </div>
    <a class="btn">Learn More <svg width="13" height="13" viewBox="0 0 24 24"><circle cx="12" cy="12" r="11" fill="#fff"/><path d="M10 7l5 5-5 5" stroke="#f39426" stroke-width="3" fill="none"/></svg></a>
  </div>
</section>

<section class="abs question">
  <h2 class="sec-title">HAVE A QUESTION?</h2>
  <span class="rule"></span>
  <p class="lead">OLVAK is a company dedicated to manufacturing and installing energy-efficient products that reduce energy consumption, save costs, and promote sustainability. Our mission is to help individuals and businesses reduce their carbon footprint while also enhancing their comfort and quality of life.</p>
  <div class="help">
    <div class="ic"><svg width="18" height="18" viewBox="0 0 24 24"><path fill="#fff" d="M6.6 10.8a15 15 0 0 0 6.6 6.6l2.2-2.2c.3-.3.7-.4 1-.2 1.1.4 2.3.6 3.6.6.6 0 1 .4 1 1V20c0 .6-.4 1-1 1A17 17 0 0 1 3 4c0-.6.4-1 1-1h3.5c.6 0 1 .4 1 1 0 1.3.2 2.5.6 3.6.1.3 0 .7-.2 1z"/></svg></div>
    <div><small>Need help now?</small><strong>Call-18000 52417</strong></div>
  </div>
  <svg class="abs" style="top:218px;left:572px" width="116" height="30" viewBox="0 0 116 30"><path d="M2 22C30 4 70 2 108 16" stroke="#fff" stroke-width="2" fill="none"/><path d="M98 8l12 9-13 5" stroke="#fff" stroke-width="2" fill="none"/></svg>
  <a class="btn">Contact Us Now</a>
</section>

<section class="abs cat-wrap">
  <div class="cat">
    <div class="tabs">
      <div class="tab active">Heating &amp; Cooling</div>
    </div>
    <div class="panel">
      <div class="photo" role="img" aria-label="Rain shower head spraying heated water in a tiled bathroom"></div>
      <div class="info">
        <svg width="72" height="72" viewBox="0 0 72 72"><path d="M34 16a20 20 0 0 0 0 40z" fill="none" stroke="#f39426" stroke-width="3"/><path d="M4 36h10M10 18l7 7M10 54l7-7M34 6v6M34 60v6" stroke="#f39426" stroke-width="3"/><path d="M38 10v52M38 36h28M42 16l20 40M62 16L42 56M50 12l-6 6M58 36l6-6M58 36l6 6" stroke="#1b5fb0" stroke-width="3"/></svg>
        <h3>Heating &amp; Cooling</h3>
        <ul>
          <li><i></i>Heat Pump</li>
          <li><i></i>Air Conditioners</li>
          <li><i></i>Swimming Pool Heat Pump</li>
          <li><i></i>Monoblock Heat Pump</li>
        </ul>
      </div>
    </div>
  </div>
</section>

<section class="abs rebates">
  <h2 class="sec-title">FULLY COMPLIANT WITH ALL GOVERNMENT REBATES</h2>
  <span class="rule"></span>
  <svg class="badge" style="left:202px" viewBox="0 0 208 208" role="img" aria-label="Locally owned badge"><circle cx="104" cy="104" r="92" fill="#2b3990"/><circle cx="104" cy="104" r="62" fill="#fff"/></svg>
  <svg class="badge" style="left:497px" viewBox="0 0 208 208" role="img" aria-label="Quality seal badge"><circle cx="104" cy="104" r="100" fill="#d9b23c"/><circle cx="104" cy="104" r="58" fill="#1c7a3c"/></svg>
  <svg class="badge" style="left:792px" viewBox="0 0 208 208" role="img" aria-label="Energy saving badge"><circle cx="104" cy="104" r="98" fill="#e3e3e3"/><circle cx="104" cy="104" r="84" fill="#fff"/></svg>
</section>

<footer class="abs footer-wrap">
  <div class="footer">
    <h4 style="left:148px">QUICK LINKS</h4>
    <ul class="links"><li>Home</li><li>Heating &amp; Cooling</li><li>Our Story</li><li>Support</li></ul>
    <h4 style="left:476px">CONTACT US</h4>
    <div class="contact">
      <div><i><svg width="11" height="11" viewBox="0 0 24 24"><path fill="#fff" d="M6.6 10.8a15 15 0 0 0 6.6 6.6l2.2-2.2c.3-.3.7-.4 1-.2 1.1.4 2.3.6 3.6.6.6 0 1 .4 1 1V20c0 .6-.4 1-1 1A17 17 0 0 1 3 4c0-.6.4-1 1-1h3.5c.6 0 1 .4 1 1 0 1.3.2 2.5.6 3.6.1.3 0 .7-.2 1z"/></svg></i><span>18000 52417</span></div>
      <div><i><svg width="11" height="9" viewBox="0 0 26 20"><rect width="26" height="20" fill="#fff"/><path d="M1 2l12 9 12-9" stroke="#1b5fb0" stroke-width="2.5" fill="none"/></svg></i><span>info@olvak.example.au</span></div>
      <div><i><svg width="10" height="12" viewBox="0 0 20 26"><path fill="#fff" d="M10 0a10 10 0 0 1 10 10c0 7-10 16-10 16S0 17 0 10A10 10 0 0 1 10 0z"/><circle cx="10" cy="10" r="3.5" fill="#1b5fb0"/></svg></i><span>Lorem ipsum dolor sit amet,<br>consectetur &nbsp;65125</span></div>
    </div>
    <h4 style="left:813px">SUBSCRIBE TO OUR BLOG</h4>
    <p class="sub-text">Enter your email address to register to our newsletter subscription</p>
    <div class="sub"><span>Email Address</span><b><svg width="16" height="16" viewBox="0 0 24 24"><path fill="#fff" d="M2 11L22 2l-8 20-3-8z"/></svg></b></div>
    <div class="social"><i></i><i></i><i></i></div>
  </div>
</footer>

<div class="abs bottombar">
  <span>Copyright© 2024 &nbsp;<u>OLVAK</u>&nbsp; | &nbsp;All Rights Reserved</span>
  <span>Terms and Conditions &nbsp; | &nbsp; Privacy Policy</span>
</div>

</body>
</html>
```